Business card design and logo needed - Photographer

I take photos of weddings, rodeos, snowmobiling.
Need a card to hand out to prospective clients.
Industry/Entity Type
Business
Contact Information for Business Card
Marcus Dolven Photography
Requirements
Must have
- Bold
Black or white base.
My website. www.MarcusDolven.example
Should not have
- camera/ lens/ aperture blades

```html
<!DOCTYPE html>
<html lang="en">
<head>
<meta charset="utf-8">
<title>Marcus Dolven Photography – Business Card</title>
<link href="https://fonts.googleapis.com/css2?family=Saira+Semi+Condensed:wght@500;600&display=swap" rel="stylesheet">
<style>
  :root {
    --backdrop: #d7dadb;
    --card: #f7f8f7;
    --ink: #1d2021;
    --teal: #3cc3a6;
    --teal-faint: #cdeee6;
  }
  * { margin: 0; padding: 0; box-sizing: border-box; }
  html, body {
    width: 1200px;
    height: 900px;
    overflow: hidden;
    background: var(--backdrop);
  }
  .card {
    position: absolute;
    left: 100px;
    top: 164px;
    width: 1000px;
    height: 572px;
    background: var(--card);
    overflow: hidden;
    box-shadow: 0 10px 30px rgba(0,0,0,0.18);
    font-family: "Saira Semi Condensed", "Arial Narrow", sans-serif;
    color: var(--ink);
  }
  .card-graphics {
    position: absolute;
    inset: 0;
  }
  .brand {
    position: absolute;
    left: 0;
    right: 0;
    top: 104px;
    display: flex;
    justify-content: center;
    align-items: center;
    gap: 22px;
  }
  .brand-mark {
    width: 58px;
    height: 58px;
    background: var(--teal);
    flex: none;
  }
  .brand-text {
    display: flex;
    flex-direction: column;
    align-items: flex-start;
  }
  .brand-name {
    font-weight: 600;
    font-size: 74px;
    line-height: 0.95;
    letter-spacing: 1px;
    color: var(--ink);
  }
  .brand-tagline {
    margin-top: 8px;
    font-weight: 600;
    font-size: 22px;
    letter-spacing: 6px;
    text-transform: uppercase;
    color: var(--ink);
  }
  .contact {
    position: absolute;
    display: flex;
    align-items: center;
    gap: 16px;
    font-weight: 600;
    color: var(--ink);
  }
  .contact svg { flex: none; }
  .contact-email {
    left: 36px;
    top: 300px;
    font-size: 26px;
  }
  .contact-web {
    left: 36px;
    top: 352px;
    font-size: 26px;
  }
  .contact-phone {
    left: 680px;
    top: 420px;
    font-size: 29px;
    letter-spacing: 1px;
  }
</style>
</head>
<body>
  <div class="card">
    <svg class="card-graphics" width="1000" height="572" viewBox="0 0 1000 572" aria-hidden="true">
      <polygon class="corner-accent" points="150,0 250,0 40,200 0,200 0,150" fill="var(--teal-faint)"/>
      <polygon class="accent-band" points="0,400 150,470 1000,486 1000,520 150,482 0,414" fill="var(--teal)"/>
    </svg>

    <div class="brand">
      <span class="brand-mark" aria-hidden="true"></span>
      <div class="brand-text">
        <h1 class="brand-name">Marcus<br>Dolven</h1>
        <p class="brand-tagline">Photography</p>
      </div>
    </div>

    <div class="contact contact-email">
      <svg width="42" height="42" viewBox="0 0 42 42" aria-hidden="true">
        <circle cx="21" cy="21" r="19" fill="none" stroke="var(--teal)" stroke-width="2.5"/>
        <rect x="10" y="14" width="22" height="15" fill="none" stroke="var(--teal)" stroke-width="2"/>
        <polyline points="10,14 21,23 32,14" fill="none" stroke="var(--teal)" stroke-width="2"/>
      </svg>
      <span>marcusdolven@example.com</span>
    </div>

    <div class="contact contact-web">
      <svg width="42" height="42" viewBox="0 0 42 42" aria-hidden="true">
        <circle cx="21" cy="21" r="19" fill="none" stroke="var(--teal)" stroke-width="2.5"/>
        <circle cx="21" cy="21" r="11" fill="none" stroke="var(--teal)" stroke-width="2"/>
        <ellipse cx="21" cy="21" rx="5" ry="11" fill="none" stroke="var(--teal)" stroke-width="2"/>
        <line x1="10" y1="21" x2="32" y2="21" stroke="var(--teal)" stroke-width="2"/>
      </svg>
      <span>www.MarcusDolven.example</span>
    </div>

    <div class="contact contact-phone">
      <svg width="44" height="44" viewBox="0 0 44 44" aria-hidden="true">
        <circle cx="22" cy="22" r="20" fill="none" stroke="var(--teal)" stroke-width="2.5"/>
        <path d="M15 11 l5 0 l2 6 l-3 2 q2 5 6 8 l2-3 l6 2 l0 5 q-2 2 -5 2 q-9 -2 -14 -12 q-2 -5 1 -10 z" fill="var(--teal)"/>
      </svg>
      <span>555 014 2288</span>
    </div>
  </div>
</body>
</html>
```